Business Card Design Project

My family and I are starting a small business. We need a business card designed for our Australian beef Exporting company. The business card needs to match the logo. The project I've launched is called "Logo design for an Australian beef export company specifically for the China market (Contest)"

Target Market(s)

Our customer
- Chinese businessmen
- In the hospitality industry
- They value Australian produce (e.g. wine and beef)

When a consumer sees it I want them to see:
- Quality
- Tradition
- Strength, Trust and partnership
- Australian made-rustic
- Chinese business culture relevance
- Family

The above elements are important to our Chinese customer. I also want the logo to look clean and professional.

The product we're selling is:
- Exporting Australian Beef to China
- We may in the future export other meats and products too.
- Clean and green Beef

Chinese cultural relevance
- The logo must be relevant to Chinese business culture

Industry/Entity Type

Business

Font styles to use
Sans Serif

Colors
0355a3
ec1f27

Requirements
Must have
• SIDE ONE
- Include the logo: it's currently being designed by ArtHive
- Elements of the business card
Phone
Email
Mobile
Web www.tallowridgemeats.asia
Favourite Cut
Full name
Role
Text (Office locations): SYDNEY KELBARRA

Colours
- Red: similar tone in the Chinese flag
- Gold: use gold to line the logo
- Blue

SIDE 2
- Image attached of the sunrise
- add text: Kelbarra Station, Queensland, Australia

```html
<!DOCTYPE html>
<html lang="en">
<head>
<meta charset="UTF-8">
<title>Business Card – Front and Back</title>
<link href="https://fonts.googleapis.com/css2?family=Quicksand:wght@400;500;700&display=swap" rel="stylesheet">
<style>
  :root {
    --page-bg: #3a3a3c;
    --card-white: #ffffff;
    --brand-red: #ec1f27;
    --brand-blue: #0355a3;
    --band-red: rgba(200, 34, 40, 0.78);
    --text-white: #ffffff;
    --photo-top: #7d7a76;
    --photo-mid: #9a6a3c;
    --photo-low: #2a2320;
    --photo-base: #161414;
    --logo-gold: #f3b437;
  }
  * { box-sizing: border-box; margin: 0; padding: 0; }
  html, body {
    width: 1200px; height: 1000px; overflow: hidden;
    background: var(--page-bg);
    font-family: "Quicksand", sans-serif;
  }
  .stage { position: relative; width: 1200px; height: 1000px; }
  .card {
    position: absolute; top: 346px;
    width: 540px; height: 308px;
    overflow: hidden;
    box-shadow: 0 10px 28px rgba(0,0,0,0.45);
  }
  .card--front { left: 40px; }
  .card--back { left: 620px; background: var(--card-white); }

  /* Front side */
  .sunrise-photo {
    position: absolute; inset: 0;
    background: linear-gradient(180deg, var(--photo-top) 0%, var(--photo-mid) 45%, var(--photo-low) 72%, var(--photo-base) 100%);
  }
  .front-band {
    position: absolute; left: 0; right: 0; top: 108px; height: 112px;
    background: var(--band-red);
  }
  .front-name {
    position: absolute; left: 0; right: 0; top: 138px;
    text-align: center;
    font-weight: 700; font-size: 44px; letter-spacing: 2px;
    color: var(--logo-gold);
  }
  .front-web {
    position: absolute; right: 28px; top: 232px;
    font-size: 17px; font-weight: 500; letter-spacing: 0.5px;
    color: var(--text-white);
  }

  /* Back side */
  .back-red {
    position: absolute; left: 0; right: 0; bottom: 0; height: 140px;
    background: var(--brand-red);
  }
  .back-logo {
    position: absolute; left: 36px; top: 92px;
    font-weight: 700; font-size: 42px; letter-spacing: 2px;
    color: var(--brand-red);
  }
  .identity { position: absolute; right: 28px; top: 24px; text-align: right; }
  .identity__name { font-size: 19px; font-weight: 500; color: var(--brand-blue); letter-spacing: 0.5px; }
  .identity__role { font-size: 13px; color: var(--brand-blue); margin-top: -2px; }
  .identity__offices {
    margin-top: 16px;
    font-size: 11px; font-weight: 700; letter-spacing: 1.6px; color: var(--brand-red);
  }
  .contacts { position: absolute; left: 30px; bottom: 16px; list-style: none; }
  .contacts li {
    display: flex; align-items: center; gap: 10px;
    font-size: 16px; color: var(--text-white); line-height: 27px;
  }
  .contacts svg { width: 16px; height: 16px; flex: none; }
  .address {
    position: absolute; right: 28px; top: 180px;
    display: flex; gap: 12px; align-items: flex-start;
  }
  .address svg { width: 14px; height: 18px; margin-top: 4px; }
  .address p { text-align: right; font-size: 14px; line-height: 19px; color: var(--text-white); }
</style>
</head>
<body>
<main class="stage">

  <section class="card card--front" aria-label="Card front">
    <div class="sunrise-photo" role="img" aria-label="Photograph of the sunrise at Kelbarra Station, Queensland, Australia"></div>
    <div class="front-band"></div>
    <div class="front-name">LOGO</div>
    <div class="front-web">www.tallowridgemeats.asia</div>
  </section>

  <section class="card card--back" aria-label="Card back">
    <div class="back-red"></div>
    <div class="back-logo">LOGO</div>

    <div class="identity">
      <div class="identity__name">FULL NAME</div>
      <div class="identity__role">Owner</div>
      <div class="identity__offices">SYDNEY KELBARRA</div>
    </div>

    <ul class="contacts">
      <li>
        <svg viewBox="0 0 16 16" aria-hidden="true"><rect x="1" y="6" width="14" height="9" rx="2" fill="#fff"/><path d="M1 6c2-4 12-4 14 0" stroke="#fff" stroke-width="2" fill="none"/><circle cx="8" cy="10.5" r="2" fill="#ec1f27"/></svg>
        01234 5678
      </li>
      <li>
        <svg viewBox="0 0 16 16" aria-hidden="true"><path d="M4 1l3 3-2 2c1 2 3 4 5 5l2-2 3 3-2 3C7 15 1 9 1 3z" fill="#fff"/></svg>
        0123 45678
      </li>
      <li>
        <svg viewBox="0 0 16 16" aria-hidden="true"><rect x="1" y="3" width="14" height="10" fill="#fff"/><path d="M1 3l7 6 7-6M1 13l5-5M15 13l-5-5" stroke="#ec1f27" stroke-width="1.4" fill="none"/></svg>
        admin@tallowridgemeats.asia
      </li>
      <li>
        <svg viewBox="0 0 16 16" aria-hidden="true"><rect x="1" y="2" width="14" height="10" rx="1" stroke="#fff" stroke-width="1.6" fill="none"/><path d="M5 15h6M8 12v3" stroke="#fff" stroke-width="1.6"/></svg>
        www.tallowridgemeats.asia
      </li>
    </ul>

    <div class="address">
      <svg viewBox="0 0 14 18" aria-hidden="true"><path d="M7 0a6 6 0 0 1 6 6c0 5-6 12-6 12S1 11 1 6a6 6 0 0 1 6-6z" fill="#fff"/><circle cx="7" cy="6" r="2.2" fill="#ec1f27"/></svg>
      <p>Suite 101, Level 1<br>Your street<br>Your city<br>2217 Australia</p>
    </div>
  </section>

</main>
</body>
</html>
```